Wordpress Design For Financial Investment Company

//** NEW WIREFRAME ADDED TO HELP WITH LAYOUT ISSUES. PLEASE REFER TO WIREFRAME IN ATTACHED FILES. NO DESIGN WILL BE CONSIDERED IF IT DOES NOT FOLLOW THE WIREFRAME. **//
//** PLEASE READ THE ENTIRE BRIEF INCLUDING ALL UPDATES TO THE BRIEF. THE CLIENT IS VERY SPECIFIC ABOUT WHAT THEY WANT AND I'VE COVERED SEVERAL THINGS IN THE UPDATES. THERE IS ALSO A VIDEO UPDATE THAT HAS SOME VALUABLE INFORMATION IN IT FOR THIS CONTEST. **//
The client is an investment advisor who needs a new website designed. The current site is http://www.velmorfield.net.
The client wants the site to be green to match the attached logo.
The home page should have relevant images in the rotator. No people hugging! This is a financial investment site, not a family counseling site.
Also, the client wants 4 buttons on the home page to highlight the 4 main areas they focus on:
Investment Advice and Education
General Financial Planning
Retirement Planning
401K Planning
The top right area of the site needs to have their phone number, a call to action, and 2 buttons.
Their phone number is 303-418-7639
The call to action should say something like "Call for a free consultation!"
The buttons need to say:
Login To Your Bluvexa Account
Login To Your Quillbrook Account
The final design should communicate professionalism, financial safety and growth.
Main navigation should be:
Home
About Us
Associates
Services
Contact
Mission Statement (Could also be "Our Mission")
This is a site that the client likes: http://www.pwkinvestmentconsulting.com/
Updates
The designs should not have:
Newsletter content. A newsletter sign up is fine
Learning Center
Calculators
Stock prices/tickers
The design should have a contact form on the page.
I have talked to my client and have some updates. I did a video update because I thought it would be easier to show what I'm trying to get across.
Reason: I am going to be extending the contest a few more days. I'm still not getting quite what I want and very few people are even trying to follow the creative brief and the updates to it.
PLEASE read the entire brief and the updates. There is also a video I made that explains everything. I've also attached a wireframe.
Thanks!
Target Market(s)
People looking for a high-end financial investment company.
Industry/Entity Type
Investment
Requirements
Must have
- !!FOLLOW THE WIREFRAME FOR LAYOUT!!
!!THEIR LOGO!!
4 buttons to highlight their main practice areas
Phone number in the top right
"Free Consultation" call to action
2 Login buttons in the top right
A contact form on the page.
Should not have
- The designs should not have:
Learning Center
Calculators
Stock prices/tickers

```html
<!DOCTYPE html>
<html lang="en">
<head>
<meta charset="utf-8">
<title>Velmorfield Financial Advisor</title>
<link rel="stylesheet" href="https://fonts.googleapis.com/css2?family=Tinos:ital,wght@0,400;0,700;1,400;1,700&family=Open+Sans:wght@400;600&display=swap">
<style>
:root{
  --teal-top:#109a8d;
  --teal-mid:#0b7a70;
  --nav-dark:#241210;
  --nav-mid:#3a2320;
  --nav-active:#b89e8e;
  --body-bg:#4b7a74;
  --card-dark:#0f3a35;
  --card-label:#22534e;
  --accent:#19c2b0;
  --accent-light:#7ff5e6;
  --paper:#f8f8f8;
  --ink:#222;
  --footer:#27504b;
  --footer-text:#ffffff;
  --logo-disc:#d8cbc0;
  --logo-ring:#3a2a24;
}
*{box-sizing:border-box;margin:0;padding:0}
html,body{width:1066px;height:1200px;overflow:hidden}
body{position:relative;background:var(--body-bg);font-family:"Open Sans",Arial,sans-serif;color:#fff}
.abs{position:absolute}
.serif{font-family:"Tinos","Times New Roman",serif}

/* header */
.header-band{left:0;top:0;width:1066px;height:141px;background:linear-gradient(180deg,var(--teal-top),var(--teal-mid))}
.login-tab{left:553px;top:0;width:491px;height:35px;background:#0a5f57;border-radius:0 0 22px 22px;display:flex;align-items:center;font-family:"Tinos",serif;font-size:17px}
.login-tab .label{display:flex;align-items:center;gap:8px;padding-left:48px;width:352px}
.login-tab .label b{font-weight:400;color:var(--accent-light);margin-left:10px}
.login-tab .alt{border-left:1px solid #0e7b70;height:35px;display:flex;align-items:center;padding-left:20px;background:#0c544d;border-radius:0 0 22px 0;flex:1}
.logo-disc{left:25px;top:12px;width:186px;height:186px;border-radius:50%;background:var(--logo-disc);border:6px solid var(--logo-ring);display:flex;align-items:center;justify-content:center;text-align:center;z-index:3}
.logo-disc span{font-family:"Tinos",serif;font-weight:700;font-size:19px;line-height:1.2;color:var(--logo-ring)}
.site-title{left:227px;top:58px;font-size:33px;letter-spacing:.5px;color:#10302c;text-shadow:0 0 1px #fff,1px 1px 0 #cfe;text-transform:uppercase}
.tagline{left:222px;top:98px;font-size:22px;font-style:italic;color:#fff}
.phone{left:886px;top:57px;display:flex;align-items:center;gap:8px;font-size:23px}

/* nav */
.nav-band{left:0;top:141px;width:1066px;height:68px;background:linear-gradient(180deg,var(--nav-mid),var(--nav-dark))}
.main-nav{left:210px;top:141px;height:68px;display:flex;font-family:"Tinos",serif;font-size:18px}
.main-nav a{display:flex;align-items:center;justify-content:center;color:#fff;text-decoration:none;border-right:1px solid #4b2f2b;height:68px}
.main-nav a.active{background:var(--nav-active);color:#1a0d0b}
.cta{left:817px;top:152px;font-family:"Tinos",serif;font-style:italic;font-weight:700;font-size:20px;line-height:21px}
.agent-photo{left:940px;top:94px;width:104px;height:115px;background:linear-gradient(180deg,#c9a98f,#3d2c25);border-radius:50px 50px 0 0;z-index:2}

/* service cards */
.card{width:250px;height:223px}
.card .photo{position:absolute;left:3px;top:3px;width:244px;height:160px;border:2px solid #9ee8de}
.card .label{position:absolute;left:0;top:166px;width:250px;height:57px;background:var(--card-label);display:flex;align-items:center;justify-content:center;font-family:"Tinos",serif;font-style:italic;font-weight:700;font-size:18px}
.card-intro{left:22px;top:221px;width:250px;height:223px;background:var(--card-dark);border-top:3px solid #fff;padding:20px 16px}
.card-intro h3{font-family:"Tinos",serif;font-size:16px;font-weight:700;margin-bottom:14px}
.card-intro p{font-family:"Tinos",serif;font-size:14px;line-height:19px;color:#dfe}
.card-intro .btn{position:absolute;top:178px;width:46px;height:45px;background:#1f524c;display:flex;align-items:center;justify-content:center}

/* slider */
.slider{left:569px;top:218px;width:477px;height:478px;border-radius:50%;overflow:hidden;border:3px solid #163f3a;background:linear-gradient(180deg,#dfe6d4 0%,#c4b6a4 45%,#6b8fb8 75%,#2d3f52 100%)}
.slider .caption{position:absolute;left:0;top:330px;width:100%;height:148px;background:rgba(20,40,38,.78);text-align:center;padding-top:10px;font-family:"Tinos",serif;font-style:italic;font-weight:700;font-size:23px;line-height:29px;color:#fff}
.slider .caption em{color:var(--accent);font-size:40px}
.dots{position:absolute;left:188px;top:452px;display:flex;gap:8px}
.dots i{width:13px;height:13px;border-radius:50%;background:var(--accent)}
.dots i:first-child{background:#e0a070}
.arrow{top:428px}

/* welcome */
.welcome{left:22px;top:713px;width:751px;height:310px;background:var(--paper);border:1px solid #ccc;color:var(--ink);padding:12px 14px}
.welcome h2{font-family:"Tinos",serif;font-size:19px;font-weight:700;padding-bottom:8px;border-bottom:2px dotted #bbb;margin-right:16px}
.welcome h4{font-weight:400;font-size:14px;margin:18px 0 16px 4px}
.welcome p{font-size:11.7px;line-height:21px;margin:0 14px 4px 4px}
.welcome-shadow{left:50px;top:1023px;width:700px;height:14px;border-radius:50%;background:radial-gradient(ellipse at top,rgba(0,0,0,.35),transparent 70%)}

/* contact form */
.contact-form{left:795px;top:713px;width:250px;height:310px;background:#4d7f79;border:1px solid #1b403c;border-radius:5px;overflow:hidden}
.contact-form .head{height:41px;background:var(--card-dark);font-family:"Tinos",serif;font-size:19px;display:flex;align-items:center;justify-content:space-between;padding:0 12px}
.contact-form .field{margin:14px 20px 0;height:30px;background:#6b9893;border:2px solid #3d6a64;border-radius:8px;padding:5px 10px;font-size:13px;color:#eef}
.contact-form .field.msg{height:76px}
.contact-form .submit{position:absolute;right:19px;top:265px;width:69px;height:28px;background:#0f3430;border:1px solid #9cc;border-radius:5px;font-size:13px;display:flex;align-items:center;justify-content:center}

/* footer */
.footer{left:0;top:1060px;width:1066px;height:140px;background:var(--footer)}
.social{left:22px;top:1081px;display:flex;gap:5px}
.social i{width:31px;height:31px;border-radius:50%;background:#1f2a28;border:2px solid #5a7a76}
.footer-nav{left:23px;top:1133px;font-size:12.5px;display:flex;gap:7px;color:#8aa}
.footer-nav a{color:#fff;text-decoration:none}
.footer-nav a.active{color:var(--accent)}
.footer-logo{left:570px;top:1069px;width:94px;height:94px;border-radius:50%;background:var(--logo-disc);border:3px solid var(--logo-ring);display:flex;align-items:center;justify-content:center;text-align:center}
.footer-logo span{font-family:"Tinos",serif;font-weight:700;font-size:10px;color:var(--logo-ring)}
.copyright{left:540px;top:1173px;font-size:12px;color:#7fa8a2}
.footer-contact{left:835px;top:1078px;font-size:12.5px;line-height:19px}
.footer-contact h5{font-size:16px;font-weight:600;margin-bottom:5px;margin-left:-2px}
</style>
</head>
<body>

<div class="abs header-band"></div>

<div class="abs login-tab">
  <div class="label">
    <svg width="22" height="18" viewBox="0 0 22 18"><circle cx="7" cy="6" r="4" fill="#fff"/><path d="M1 17c0-5 12-5 12 0z" fill="#fff"/><path d="M13 2h8v6h-5l-3 2z" fill="#fff"/></svg>
    Login To Your Account : <b>Bluvexa</b>
  </div>
  <div class="alt">Quillbrook</div>
</div>

<div class="abs logo-disc"><span>VELMORFIELD<br>Financial, Inc.</span></div>

<div class="abs site-title serif">Velmorfield Financial Advisor</div>
<div class="abs tagline serif">“Always do right. This will gratify some people &amp; astonish the rest.”</div>

<div class="abs phone serif">
  <svg width="20" height="24" viewBox="0 0 20 24"><rect x="3" y="2" width="14" height="20" rx="3" fill="none" stroke="#fff" stroke-width="2"/><rect x="7" y="17" width="6" height="2" fill="#fff"/></svg>
  303-418-7639
</div>

<div class="abs nav-band"></div>
<nav class="abs main-nav">
  <a class="active" href="#" style="width:88px">Home</a>
  <a href="#" style="width:128px">About Us</a>
  <a href="#" style="width:135px">Associates</a>
  <a href="#" style="width:112px">Services</a>
  <a href="#" style="width:110px">Contact</a>
</nav>
<div class="abs cta">Call for a free<br>consultation!</div>
<div class="abs agent-photo" role="img" aria-label="Photo of a support agent wearing a headset"></div>

<div class="abs card-intro">
  <h3>Lorem ipsum dolor</h3>
  <p>Lorem ipsum dolor sit amet, consectetur adipiscing elit. Mauris vestibulum consectetur elit. Fusce vitae dui sit amet tortor mattis tincidunt sed sit amet velit</p>
  <div class="btn" style="left:150px">
    <svg width="18" height="18" viewBox="0 0 18 18"><circle cx="7" cy="7" r="5" fill="none" stroke="#fff" stroke-width="2.5"/><path d="M11 11l5 5" stroke="#fff" stroke-width="3"/></svg>
  </div>
  <div class="btn" style="left:204px">
    <svg width="20" height="20" viewBox="0 0 20 20"><rect x="1" y="9" width="10" height="6" rx="3" transform="rotate(-45 6 12)" fill="none" stroke="#fff" stroke-width="2"/><rect x="9" y="5" width="10" height="6" rx="3" transform="rotate(-45 14 8)" fill="none" stroke="#fff" stroke-width="2"/></svg>
  </div>
</div>

<div class="abs card" style="left:297px;top:221px">
  <div class="photo" role="img" aria-label="Photo of a child in a helmet and suit holding a ruler" style="background:linear-gradient(180deg,#bfc9cc,#e6d3b2)"></div>
  <div class="label">General Financial Planning</div>
</div>
<div class="abs card" style="left:22px;top:469px">
  <div class="photo" role="img" aria-label="Photo of a retired couple reviewing documents with an advisor" style="background:linear-gradient(135deg,#8a6f5c,#e7dcd2 60%,#c9b7a8)"></div>
  <div class="label">Retirement Planning</div>
</div>
<div class="abs card" style="left:297px;top:469px">
  <div class="photo" role="img" aria-label="Photo of piggy banks in front of a retirement chalkboard" style="background:linear-gradient(180deg,#2b2f36,#3a3f48 60%,#d9a0b4)"></div>
  <div class="label">401K Planning</div>
</div>

<div class="abs slider" role="img" aria-label="Rotator photo of a smiling retired couple">
  <div class="caption">Only <em>42%</em> Of Americans Know<br>How Mutch Money to<br>save for retirement</div>
  <div class="dots"><i></i><i></i><i></i><i></i><i></i></div>
</div>
<svg class="abs arrow" style="left:574px" width="24" height="44" viewBox="0 0 24 44"><path d="M20 3L4 22l16 19" fill="none" stroke="#0f2624" stroke-width="5"/></svg>
<svg class="abs arrow" style="left:1014px" width="24" height="44" viewBox="0 0 24 44"><path d="M4 3l16 19L4 41" fill="none" stroke="#0f2624" stroke-width="5"/></svg>

<section class="abs welcome">
  <h2>WELCOME TO OUR SITE!</h2>
  <h4>About Velmorfield Financial, Inc.</h4>
  <p>Lorem ipsum dolor sit amet, consectetur adipiscing elit. Vivamus sodales consectetur viverra. Donec turpis ipsum, pretium ut adipiscing at, viverra nec ligula. Nam eros eros, laoreet sed congue nec, viverra et erat. Aenean scelerisque, elit dictum faucibus porttitor, sem orci feugiat ligula, facilisis sagittis turpis felis in tortor. Maecenas quis quam augue. Duis mollis hendrerit ultricies. Duis auctor volutpat hendrerit.</p>
  <p>Lorem ipsum dolor sit amet, consectetur adipiscing elit. Vivamus sodales consectetur viverra. Donec turpis ipsum, pretium ut adipiscing at, viverra nec ligula. Nam eros eros, laoreet sed congue nec, viverra et erat. Aenean scelerisque, elit dictum faucibus porttitor, sem orci feugiat ligula, facilisis sagittis turpis felis in tortor. Maecenas quis quam augue. Duis mollis hendrerit ultricies. Duis auctor volutpat hendrerit. lorem ipsum dolor sit amet, consectetur adipiscing elit.</p>
</section>
<div class="abs welcome-shadow"></div>

<form class="abs contact-form">
  <div class="head">CONTACT FORM
    <svg width="22" height="24" viewBox="0 0 22 24"><rect x="4" y="1" width="16" height="22" rx="2" fill="#fff"/><path d="M8 7h9M8 11h9M8 15h9" stroke="#0f3a35" stroke-width="1.5"/><path d="M2 5h4M2 10h4M2 15h4M2 20h4" stroke="#fff" stroke-width="2"/></svg>
  </div>
  <div class="field">Name</div>
  <div class="field">Phone</div>
  <div class="field">Email</div>
  <div class="field msg">Message</div>
  <div class="submit">Submit</div>
</form>

<footer>
  <div class="abs footer"></div>
  <div class="abs social" aria-label="Social links"><i></i><i></i><i></i><i></i><i></i><i></i><i></i></div>
  <div class="abs footer-nav">
    <a class="active" href="#">Home</a>/<a href="#">About Us</a>/<a href="#">Associates</a>/<a href="#">Services</a>/<a href="#">Our Mission</a>/<a href="#">Contact Us</a>
  </div>
  <div class="abs footer-logo"><span>VELMORFIELD<br>Financial, Inc.</span></div>
  <div class="abs copyright">© 2013 All Rights Reserved</div>
  <div class="abs footer-contact">
    <h5>Contact Us</h5>
    2280 Larkstone Parkway #412<br>
    Fernhollow, CO 80947<br>
    Phone: 303-418-7639 800-555-0184<br>
    Fax: 303-555-0127
  </div>
</footer>

</body>
</html>
```